Memorial Ledger Suite (Web Design)

Design with your logo. Background in black or dark. Elegant style, it's a website for professional people only. Our company provides a cloud software manager for Funeral Services Companies.

Target Market(s)

Professional of Funeral Services.

Coding

Coded - Design and coding required

Number of Pages Required

3 page

Font styles to use
Sans Serif

Colors
fbee3d
000000
5c5c5c

Requirements
Must have
• Design of the website should be similar to our logo colors.

```html
<!DOCTYPE html>
<html lang="en">
<head>
<meta charset="utf-8">
<title>Memorial Ledger Suite</title>
<link rel="stylesheet" href="https://fonts.googleapis.com/css2?family=Poppins:wght@400;500;600;700;800&family=Open+Sans:wght@400;600;700&display=swap">
<style>
:root{
  --yellow:#fbee3d;
  --black:#000000;
  --grey:#5c5c5c;
  --light:#ececec;
  --white:#ffffff;
  --text:#333333;
}
*{box-sizing:border-box;margin:0;padding:0}
html,body{width:1200px;height:3696px;overflow:hidden;background:var(--white)}
body{position:relative;font-family:"Open Sans",sans-serif;color:var(--text)}
.abs{position:absolute}
h1,h2,h3,h4,.brand{font-family:"Poppins",sans-serif}

/* header */
.site-header{left:0;top:0;width:1200px;height:128px;background:var(--white)}
.brand{left:110px;top:30px;font-weight:700;font-size:30px;line-height:34px;color:var(--grey);display:flex;align-items:center;gap:12px}
.brand-mark{width:26px;height:26px;border-radius:50%;background:var(--yellow);flex:none}
.follow{left:686px;top:28px;display:flex;align-items:center;gap:8px;font-size:13px;font-weight:600;color:var(--text)}
.follow .dot{width:28px;height:28px;border-radius:50%;background:#1b5fa8}
.call{left:926px;top:22px;display:flex;align-items:center;gap:14px}
.call small{display:block;font-size:12px;font-weight:600;color:var(--text)}
.call strong{display:block;font-family:"Poppins",sans-serif;font-size:20px;font-weight:600;color:var(--black);line-height:22px}
.main-nav{left:525px;top:84px;display:flex;gap:30px;font-size:15px;color:var(--text);align-items:center}

/* hero */
.hero{left:0;top:128px;width:1200px;height:557px;background:radial-gradient(ellipse at 30% 60%,#6b3a2a 0%,#3a2620 40%,#1b1513 75%)}
.hero-title{left:0;top:378px;width:1200px;text-align:center;color:var(--white);font-size:50px;line-height:60px;font-weight:700;letter-spacing:.5px}
.hero-dots{left:1137px;top:372px;display:flex;flex-direction:column;gap:11px}
.hero-dots span{width:16px;height:16px;border-radius:50%;background:var(--white)}
.hero-dots span.active{border:3px solid var(--white);background:transparent}

/* welcome */
.welcome{left:123px;top:592px;width:957px;height:455px;background:var(--white);box-shadow:0 4px 18px rgba(0,0,0,.18)}
.welcome-text{left:65px;top:42px;width:460px}
.welcome-text h4{font-size:17px;font-weight:600;color:var(--black)}
.welcome-text h2{font-size:31px;line-height:34px;font-weight:800;color:var(--black);margin-bottom:12px}
.welcome-text p{font-size:13.5px;line-height:27px;color:#444}
.btn{display:inline-block;background:var(--yellow);color:var(--black);font-family:"Poppins",sans-serif;font-weight:700;font-size:15px;text-transform:uppercase}
.welcome .btn{margin-top:20px;padding:10px 24px}
.welcome-img{left:549px;top:33px;width:381px;height:390px;background:radial-gradient(circle at 50% 45%,#f29a6a 0%,#b0473c 35%,#3b2740 70%,#1d1b2c 100%)}

/* services */
.services{left:0;top:1135px;width:1200px;height:848px;background:var(--light)}
.section-title{width:1200px;left:0;text-align:center;font-size:34px;font-weight:800;color:var(--black)}
.service-card{width:298px;height:239px;background:var(--white);border-radius:6px;padding:40px 25px 0;box-shadow:0 1px 4px rgba(0,0,0,.1)}
.service-card .icon{width:50px;height:50px;margin-bottom:22px}
.service-card h3{font-size:19px;font-weight:700;color:var(--black);margin-bottom:4px}
.service-card p{font-size:14px;line-height:27px;color:#555}
.service-card.featured{background:var(--black)}
.service-card.featured h3{color:var(--yellow)}
.service-card.featured p{color:var(--white)}
.services .btn{left:481px;top:730px;width:238px;height:50px;line-height:50px;text-align:center;font-size:15px}

/* gallery */
.gallery-item{background:#888}
.carousel-dots{left:570px;top:2562px;display:flex;gap:12px}
.carousel-dots span{width:16px;height:16px;border-radius:50%;background:#bdbdbd}
.carousel-dots span.active{background:var(--black)}

/* quote */
.quote{left:0;top:2640px;width:625px;height:662px;background:var(--yellow)}
.map{left:625px;top:2640px;width:575px;height:660px;background:linear-gradient(160deg,#d8d8d2,#bdbdb6)}
.quote h2{left:150px;top:80px;font-size:32px;font-weight:800;color:var(--black)}
.field{left:150px;width:445px;border-bottom:2px solid var(--black);font-size:15px;color:var(--black);padding-bottom:8px;display:flex;align-items:center;gap:10px}
.submit{left:150px;top:490px;width:235px;height:68px;border:3px solid var(--black);font-family:"Poppins",sans-serif;font-weight:700;font-size:22px;color:var(--black);text-align:center;line-height:62px;text-transform:uppercase}

/* footer */
.footer-bg{left:0;top:3248px;width:1200px;height:448px}
.footer-brand{left:128px;top:3380px;width:400px;font-size:38px;line-height:46px;font-weight:700;color:var(--yellow);display:flex;align-items:center;gap:16px}
.footer-brand .brand-mark{width:36px;height:36px}
.footer-col h4{font-size:21px;font-weight:600;color:var(--white);margin-bottom:18px;text-transform:uppercase}
.footer-col li{list-style:none;font-size:14px;color:var(--white);margin-bottom:14px}
.contact-row{display:flex;gap:14px;color:var(--white);font-size:14px;line-height:26px;margin-bottom:18px}
.contact-row svg{flex:none;margin-top:5px}
.copyright{left:120px;top:3640px;font-size:13.5px;color:var(--white)}
.footer-social{left:935px;top:3632px;display:flex;gap:8px}
.footer-social span{width:32px;height:32px;border-radius:50%;border:2px solid var(--white)}
</style>
</head>
<body>

<header class="site-header abs">
  <div class="brand abs"><span class="brand-mark"></span>Memorial Ledger Suite</div>
  <div class="follow abs">FOLLOW US: <span class="dot"></span><span class="dot" style="background:#1da1f2"></span><span class="dot" style="background:#0a66c2"></span></div>
  <div class="call abs">
    <svg width="34" height="34" viewBox="0 0 24 24"><rect width="24" height="24" rx="3" fill="#000"/><path d="M7 5l3 3-1.5 2a9 9 0 0 0 5 5L15.5 13.5l3 3-2 2.5C10 18 6 14 4.5 8z" fill="#fff"/></svg>
    <div><small>Call Us Now:</small><strong>555-014-2290</strong></div>
  </div>
  <nav class="main-nav abs">
    <span>Presentation</span><span>Services</span><span>Gallery</span><span>Contact</span><span>Nederlands Versie</span>
    <svg width="18" height="18" viewBox="0 0 20 20"><circle cx="8" cy="8" r="6" fill="none" stroke="#000" stroke-width="2.5"/><path d="M12.5 12.5L18 18" stroke="#000" stroke-width="2.5"/></svg>
  </nav>
</header>

<section class="hero abs" role="img" aria-label="Photo of a man in a dark suit with folded hands at a funeral service"></section>
<h1 class="hero-title abs">MEMORIAL LEDGER SUITE</h1>
<div class="hero-dots abs"><span class="active"></span><span></span><span></span></div>

<section class="welcome abs">
  <div class="welcome-text abs">
    <h4>WELCOME TO</h4>
    <h2>MEMORIAL<br>LEDGER SUITE</h2>
    <p>Lorem ipsum dolor sit amet, consectetur adipiscing elit, sed do eiusmod tempor incididunt ut labore et dolore magna aliqua. Ut enim ad minim veniam, quis nostrud exercitation ullamco laboris nisi ut aliquip ex ea commodo consequat. Duis aute irure dolor in reprehenderit in voluptate velit esse cillum dolore eu fugiat nulla pariatur. Excepteur sint occaecat cupidatat non proident, sunt in culpa qui officia deserunt mollit anim id est laborum.</p>
    <span class="btn">Read More</span>
  </div>
  <div class="welcome-img abs" role="img" aria-label="Photo of a hand touching a glowing digital security padlock interface"></div>
</section>

<section class="services abs">
  <h2 class="section-title abs" style="top:70px">OUR SERVICES</h2>

  <article class="service-card abs" style="left:126px;top:158px">
    <svg class="icon" viewBox="0 0 50 50"><rect width="50" height="50" rx="4" fill="#000"/><rect x="10" y="13" width="30" height="20" fill="none" stroke="#fff" stroke-width="2"/><path d="M7 37h36" stroke="#fff" stroke-width="3"/></svg>
    <h3>Online Software</h3><p>Lorem ipsum dolor sit amet, consectetuer adipiscing elit sed diam nonummy .</p>
  </article>
  <article class="service-card featured abs" style="left:451px;top:158px">
    <svg class="icon" viewBox="0 0 50 50"><rect width="50" height="50" rx="4" fill="#fbee3d"/><rect x="13" y="10" width="20" height="28" fill="none" stroke="#000" stroke-width="2"/><path d="M17 17h12M17 23h12M17 29h7M30 34l10-12" stroke="#000" stroke-width="2"/></svg>
    <h3>Personalized Documents</h3><p>Lorem ipsum dolor sit amet, consectetuer adipiscing elit sed diam nonummy .</p>
  </article>
  <article class="service-card abs" style="left:777px;top:158px">
    <svg class="icon" viewBox="0 0 50 50"><rect width="50" height="50" rx="4" fill="#000"/><rect x="12" y="11" width="22" height="28" fill="none" stroke="#fff" stroke-width="2"/><circle cx="33" cy="32" r="7" fill="#000" stroke="#fff" stroke-width="2"/><path d="M16 18h14M16 24h10" stroke="#fff" stroke-width="2"/></svg>
    <h3>Billing</h3><p>Lorem ipsum dolor sit amet, consectetuer adipiscing elit sed diam nonummy .</p>
  </article>
  <article class="service-card abs" style="left:126px;top:424px">
    <svg class="icon" viewBox="0 0 50 50"><rect width="50" height="50" rx="4" fill="#000"/><rect x="9" y="14" width="32" height="22" rx="2" fill="none" stroke="#fff" stroke-width="2"/><circle cx="18" cy="23" r="3" fill="#fff"/><path d="M26 21h10M26 27h10M13 31h10" stroke="#fff" stroke-width="2"/></svg>
    <h3>Electronic identity card</h3><p>Lorem ipsum dolor sit amet, consectetuer adipiscing elit sed diam nonummy .</p>
  </article>
  <article class="service-card abs" style="left:451px;top:424px">
    <svg class="icon" viewBox="0 0 50 50"><rect width="50" height="50" rx="4" fill="#000"/><rect x="13" y="9" width="22" height="9" fill="none" stroke="#fff" stroke-width="2"/><rect x="13" y="20" width="22" height="9" fill="none" stroke="#fff" stroke-width="2"/><rect x="13" y="31" width="22" height="9" fill="none" stroke="#fff" stroke-width="2"/></svg>
    <h3>Archiving</h3><p>Lorem ipsum dolor sit amet, consectetuer adipiscing elit sed diam nonummy .</p>
  </article>
  <article class="service-card abs" style="left:777px;top:424px">
    <svg class="icon" viewBox="0 0 50 50"><rect width="50" height="50" rx="4" fill="#000"/><rect x="9" y="11" width="32" height="22" fill="none" stroke="#fff" stroke-width="2"/><circle cx="25" cy="22" r="5" fill="none" stroke="#fff" stroke-width="2"/><path d="M19 39h12M25 33v6" stroke="#fff" stroke-width="2"/></svg>
    <h3>Display on screens</h3><p>Lorem ipsum dolor sit amet, consectetuer adipiscing elit sed diam nonummy .</p>
  </article>

  <span class="btn abs">View More Services</span>
</section>

<section class="gallery">
  <h2 class="section-title abs" style="top:2058px">OUR GALLERY</h2>
  <div class="gallery-item abs" style="left:128px;top:2157px;width:464px;height:343px;background:linear-gradient(135deg,#e9e4dc,#5b6f84 55%,#1d2a3a)" role="img" aria-label="Photo of a businessman using a digital tablet interface"></div>
  <div class="gallery-item abs" style="left:600px;top:2157px;width:231px;height:165px;background:linear-gradient(135deg,#f1f1ef,#b8c3cf)" role="img" aria-label="Photo of charts and documents on a desk"></div>
  <div class="gallery-item abs" style="left:840px;top:2157px;width:231px;height:165px;background:linear-gradient(180deg,#c9dbe8 0%,#7c9a5c 45%,#4f6a38 100%)" role="img" aria-label="Photo of rows of white grave markers in a cemetery"></div>
  <div class="gallery-item abs" style="left:600px;top:2335px;width:231px;height:165px;background:radial-gradient(circle at 50% 60%,#f3c35a 0%,#8a4a16 35%,#1c1008 80%)" role="img" aria-label="Photo of a lit candle in a dark church"></div>
  <div class="gallery-item abs" style="left:840px;top:2335px;width:231px;height:165px;background:linear-gradient(135deg,#b56a5a,#e8d6cf 60%,#f3ece8)" role="img" aria-label="Photo of hands typing on a laptop"></div>
  <div class="carousel-dots abs"><span class="active"></span><span></span><span></span></div>
</section>

<section class="quote abs">
  <h2 class="abs">GET A QUOTE</h2>
  <div class="field abs" style="top:150px">
    <svg width="14" height="14" viewBox="0 0 14 14"><circle cx="7" cy="4" r="3" fill="#000"/><path d="M1 14a6 6 0 0 1 12 0z" fill="#000"/></svg>Name</div>
  <div class="field abs" style="top:228px">
    <svg width="15" height="12" viewBox="0 0 15 12"><rect x="1" y="1" width="13" height="10" fill="none" stroke="#000" stroke-width="1.5"/><path d="M1 1l6.5 5L14 1" fill="none" stroke="#000" stroke-width="1.5"/></svg>Email</div>
  <div class="field abs" style="top:305px">
    <svg width="14" height="14" viewBox="0 0 24 24"><path d="M6 2l4 4-2 3a11 11 0 0 0 7 7l3-2 4 4-3 4C9 22 2 15 2 5z" fill="#000"/></svg>Phone Number</div>
  <div class="field abs" style="top:355px;height:98px;align-items:flex-start">
    <svg width="14" height="13" viewBox="0 0 14 13" style="margin-top:4px"><path d="M1 1h12v8H5l-4 3z" fill="#000"/></svg>Message...</div>
  <div class="submit abs">Submit</div>
</section>
<div class="map abs" role="img" aria-label="Map of the office location with a home marker pin"></div>

<svg class="footer-bg abs" width="1200" height="448" viewBox="0 0 1200 448"><polygon points="0,54 1200,0 1200,448 0,448" fill="#000"/></svg>

<footer>
  <div class="footer-brand brand abs"><span class="brand-mark"></span><span>Memorial Ledger<br>Suite</span></div>
  <div class="footer-col abs" style="left:568px;top:3338px">
    <h4>Quick Links</h4>
    <ul><li>Presentation</li><li>Services</li><li>Gallery</li><li>Contact</li><li>Nederlands Versie</li></ul>
  </div>
  <div class="footer-col abs" style="left:833px;top:3338px;width:270px">
    <h4>Contact Us</h4>
    <div class="contact-row"><svg width="14" height="18" viewBox="0 0 14 18"><path d="M7 1a6 6 0 0 1 6 6c0 4-6 10-6 10S1 11 1 7a6 6 0 0 1 6-6z" fill="none" stroke="#fff" stroke-width="1.5"/><circle cx="7" cy="7" r="2" fill="#fff"/></svg><span># 10, Nemo enim ipsam voluptatem quia voluptas sit aspernatur aut odit</span></div>
    <div class="contact-row"><svg width="16" height="16" viewBox="0 0 24 24"><path d="M6 2l4 4-2 3a11 11 0 0 0 7 7l3-2 4 4-3 4C9 22 2 15 2 5z" fill="none" stroke="#fff" stroke-width="1.6"/></svg><span>555-014-2290</span></div>
    <div class="contact-row"><svg width="17" height="13" viewBox="0 0 15 12"><rect x="1" y="1" width="13" height="10" fill="none" stroke="#fff" stroke-width="1.2"/><path d="M1 1l6.5 5L14 1" fill="none" stroke="#fff" stroke-width="1.2"/></svg><span>info@memorialledgersuite.com</span></div>
  </div>
  <p class="copyright abs">© 2019 Company Name &nbsp;|&nbsp; All Rights Reserved</p>
  <div class="footer-social abs"><span></span><span></span><span></span><span></span></div>
</footer>

</body>
</html>
```